Coffee Roaster Needs A Postcard Design

I am coffee roaster ( a home business) and I would like to create a neighborhood delivery service. Once a month I would delivery fresh roasted coffee to my neighbors. I would like to create a postcard to advertise the coffee delivery service.

Preferences: The postcard would be very simple, primarily black and white ( a little color) with visuals; fresh roasted coffee beans, delivered to the doorstep, a great cup of coffee. Simple steps, 1 2 & 3.

I have a website the postcard advertisement should flow with the site : www.brinmoorcoffeeworks.com

Target Market(s)

Upper class residential neighborhood

Industry/Entity Type

Business

Font styles to use
Serif

Colors
f04a50

Requirements
Must have
• Images _ Coffee Beans

```html
<!DOCTYPE html>
<html lang="en">
<head>
<meta charset="utf-8">
<title>Brinmoor Coffee Works – Postcard</title>
<link rel="stylesheet" href="https://fonts.googleapis.com/css2?family=Cinzel:wght@400;700&display=swap">
<style>
  :root {
    --backdrop: #e4e4e4;
    --card: #ffffff;
    --ink: #231f20;
    --accent: #f04a50;
    --bean-dark: #6b3f1d;
    --bean-light: #a7714a;
    --paper-text: #ffffff;
  }
  * { box-sizing: border-box; margin: 0; padding: 0; }
  html, body {
    width: 1200px;
    height: 816px;
    overflow: hidden;
    background: var(--backdrop);
  }
  .canvas {
    position: relative;
    width: 1200px;
    height: 816px;
  }
  .postcard {
    position: absolute;
    left: 105px;
    top: 29px;
    width: 990px;
    height: 758px;
    background: var(--card);
    overflow: hidden;
    box-shadow: 0 2px 10px rgba(0,0,0,0.12);
    font-family: "Cinzel", serif;
    color: var(--ink);
  }
  .brand {
    position: absolute;
    left: 96px;
    top: 40px;
    width: 222px;
    display: flex;
    flex-direction: column;
    align-items: center;
    gap: 16px;
  }
  .brand-mark {
    width: 22px;
    height: 22px;
    background: var(--ink);
  }
  .brand-name {
    font-family: "Cinzel", serif;
    font-weight: 700;
    font-size: 27px;
    line-height: 1.3;
    letter-spacing: 4px;
    text-align: center;
    color: var(--ink);
    text-transform: uppercase;
  }
  .offer {
    position: absolute;
    left: 23px;
    width: 400px;
    top: 265px;
    list-style: none;
    text-align: center;
  }
  .offer li {
    font-size: 39px;
    line-height: 1;
    height: 90px;
    letter-spacing: 1px;
    font-weight: 400;
  }
  .offer li.offer-highlight { font-weight: 700; }
  .artwork {
    position: absolute;
    left: 0;
    top: 0;
    width: 990px;
    height: 758px;
  }
  .footer-band {
    position: absolute;
    left: 0;
    top: 714px;
    width: 990px;
    height: 39px;
    background: var(--ink);
    display: flex;
    align-items: center;
    justify-content: center;
  }
  .footer-url {
    font-family: "Cinzel", serif;
    font-size: 15px;
    letter-spacing: 6px;
    color: var(--paper-text);
    text-transform: uppercase;
  }
</style>
</head>
<body>
<main class="canvas">
  <section class="postcard">
    <svg class="artwork" width="990" height="758" viewBox="0 0 990 758" xmlns="http://www.w3.org/2000/svg">
      <defs>
        <clipPath id="art-area">
          <rect x="0" y="0" width="990" height="714"/>
        </clipPath>
        <radialGradient id="bean-field" cx="965" cy="673" r="480" gradientUnits="userSpaceOnUse">
          <stop offset="0" stop-color="var(--accent)" stop-opacity="0.55"/>
          <stop offset="0.35" stop-color="#c9835c" stop-opacity="0.45"/>
          <stop offset="1" stop-color="#8a5630" stop-opacity="0.35"/>
        </radialGradient>
        <path id="slogan-arc" d="M 430 673 A 535 535 0 0 1 965 138"/>
      </defs>
      <g clip-path="url(#art-area)">
        <circle cx="965" cy="673" r="470" fill="url(#bean-field)"
                role="img" aria-label="Illustration of brown coffee beans scattered around a steaming red coffee cup"/>
      </g>
      <text class="slogan" font-family="Cinzel, serif" font-size="46" fill="var(--accent)" letter-spacing="6">
        <textPath href="#slogan-arc" startOffset="12" textLength="800" lengthAdjust="spacing">A GREAT CUP OF COFFEE!</textPath>
      </text>
    </svg>

    <div class="brand">
      <span class="brand-mark" aria-hidden="true"></span>
      <p class="brand-name">Brinmoor<br>Coffee<br>Works</p>
    </div>

    <ul class="offer">
      <li>Fresh Roasted</li>
      <li class="offer-highlight">Coffee Beans</li>
      <li>Delivered</li>
      <li>To the</li>
      <li>Doorstep</li>
    </ul>

    <footer class="footer-band">
      <span class="footer-url">www.brinmoorcoffeeworks.com</span>
    </footer>
  </section>
</main>
</body>
</html>
```